New Business Card

Would like a shiny card with Metallic logo raised on th front. Address 418 Kestwick Lane, Toronto Ontario M4T2B8, phone 416 555 0382, email kmvc@lorentel.ca and web www.kmvc.ca on the back in right and left lower corners balanced. Top of back should say Personalized Care for Pet's and their People centered. Leaving space on the back to write. Horizontal placement

```html
<!DOCTYPE html>
<html lang="en">
<head>
<meta charset="utf-8">
<title>Kestwick Mews Veterinary Clinic – Business Card</title>
<link href="https://fonts.googleapis.com/css2?family=Arimo:wght@400&family=Caveat:wght@400&family=Josefin+Sans:wght@400;600&display=swap" rel="stylesheet">
<style>
  :root {
    --backdrop: #e6e6e6;
    --card: #ffffff;
    --band: #9bafb8;
    --ink: #2b2b2b;
    --mark: #5a5a5a;
    --rule: #555555;
    --icon: #4a4a4a;
  }
  html, body {
    margin: 0;
    padding: 0;
    width: 1200px;
    height: 1200px;
    overflow: hidden;
    background: var(--backdrop);
  }
  .canvas {
    position: relative;
    width: 1200px;
    height: 1200px;
  }
  .card {
    position: absolute;
    left: 290px;
    width: 642px;
    height: 406px;
    background: var(--card);
    box-shadow: 0 6px 18px rgba(0,0,0,0.18);
    overflow: hidden;
  }
  .card--front { top: 182px; }
  .card--back  { top: 694px; }

  /* Front */
  .brand {
    position: absolute;
    left: 0;
    right: 0;
    top: 70px;
    display: flex;
    flex-direction: column;
    align-items: center;
  }
  .brand__dot {
    width: 130px;
    height: 130px;
    border-radius: 50%;
    background: var(--mark);
    margin-bottom: 34px;
  }
  .brand__name {
    margin: 0;
    font-family: "Josefin Sans", sans-serif;
    font-weight: 600;
    font-size: 42px;
    line-height: 1;
    letter-spacing: 1px;
    text-transform: uppercase;
    color: var(--ink);
    white-space: nowrap;
  }
  .brand__sub {
    display: flex;
    align-items: center;
    gap: 12px;
    width: 456px;
    margin-top: 8px;
    font-family: "Josefin Sans", sans-serif;
    font-weight: 600;
    font-size: 18px;
    letter-spacing: 1px;
    text-transform: uppercase;
    color: var(--ink);
    white-space: nowrap;
  }
  .brand__sub::before,
  .brand__sub::after {
    content: "";
    flex: 1;
    height: 1.5px;
    background: var(--rule);
  }

  /* Back */
  .tagline {
    position: absolute;
    top: 0;
    left: 0;
    right: 0;
    height: 71px;
    margin: 0;
    background: var(--band);
    font-family: "Caveat", cursive;
    font-weight: 400;
    font-size: 40px;
    line-height: 71px;
    text-align: center;
    white-space: nowrap;
    color: #111;
  }
  .contact-band {
    position: absolute;
    left: 0;
    right: 0;
    bottom: 0;
    height: 89px;
    background: var(--band);
    display: flex;
    justify-content: space-between;
    align-items: center;
    padding: 0 14px 0 10px;
    box-sizing: border-box;
    font-family: "Arimo", sans-serif;
    font-size: 17px;
    line-height: 22px;
    color: var(--ink);
  }
  .address {
    font-style: normal;
  }
  .contact-list {
    list-style: none;
    margin: 0;
    padding: 0;
    text-align: right;
  }
  .contact-list li {
    display: flex;
    justify-content: flex-end;
    align-items: center;
    gap: 6px;
  }
  .contact-icon {
    width: 15px;
    height: 15px;
    flex: none;
  }
  .contact-icon path, .contact-icon rect, .contact-icon polyline {
    fill: none;
    stroke: var(--icon);
    stroke-width: 1.3;
    stroke-linejoin: round;
    stroke-linecap: round;
  }
</style>
</head>
<body>
<main class="canvas">

  <section class="card card--front" aria-label="Card front">
    <div class="brand">
      <div class="brand__dot" aria-hidden="true"></div>
      <h1 class="brand__name">Kestwick Mews</h1>
      <p class="brand__sub">Veterinary Clinic</p>
    </div>
  </section>

  <section class="card card--back" aria-label="Card back">
    <p class="tagline">Personalized Care for Pets and their People</p>

    <div class="contact-band">
      <address class="address">
        418 Kestwick Lane<br>
        Toronto Ontario<br>
        M4T2B8
      </address>
      <ul class="contact-list">
        <li>416 555 0382
          <svg class="contact-icon" viewBox="0 0 16 16" aria-hidden="true">
            <path d="M4 1.5 L6 4.5 L4.8 6.2 C5.8 8.3 7.7 10.2 9.8 11.2 L11.5 10 L14.5 12 L13.2 14.2 C8 14 2 8 1.8 2.8 Z"/>
          </svg>
        </li>
        <li>kmvc@lorentel.ca
          <svg class="contact-icon" viewBox="0 0 16 16" aria-hidden="true">
            <rect x="1.5" y="3.5" width="13" height="9"/>
            <polyline points="1.5,3.5 8,9 14.5,3.5"/>
          </svg>
        </li>
        <li>www.kmvc.ca
          <svg class="contact-icon" viewBox="0 0 16 16" aria-hidden="true">
            <polyline points="1.5,8 8,2 14.5,8"/>
            <path d="M3.5 6.5 V14 H12.5 V6.5"/>
            <rect x="6.5" y="10" width="3" height="4"/>
          </svg>
        </li>
      </ul>
    </div>
  </section>

</main>
</body>
</html>
```